Emerging Music artist seeks freely creative EP Cover design

What do you envision when you think of an album cover? Lets see it. I seek a professional looking design that will make the cover (front and related back) of my debut ep catch the eye of people walking past it on the shelf. With or without color, symbolic reference or not, simple or complex doesn't matter; creative freedom is welcomed and encouraged. The only requirement is that the attached symbol is included somewhere in the design (whether that means you make it the upfront centerpiece or somewhere less blatant in the design)... I'll add song files so you can get a reference of the type of songs going on the cd... My stage name is "Dane Olsk" and it is a self titled album.

Target Market(s)

pop music scene

Industry/Entity Type

It Professional

Requirements
Must have
• Project must include the attached symbol. (Don't use what I actually drew though; I'd much rather you draw it. I am not an artist)
Nice to have
• Anything goes that you might see in other creative CD cover designs.
Should not have
• Anything crude or inappropriate.

```html
<!DOCTYPE html>
<html lang="en">
<head>
<meta charset="utf-8">
<title>Dane Olsk – EP Cover, Front and Back</title>
<link rel="stylesheet" href="https://fonts.googleapis.com/css2?family=Special+Elite&display=swap">
<style>
  :root {
    --smoke-white: #f2f2f2;
    --smoke-light: #d6d6d6;
    --smoke-grey: #9a9a9a;
    --smoke-dark: #1c1c1c;
    --ink-black: #0b0b0b;
    --mark-red: #b53b3d;
    --mark-red-back: #c4484a;
    --type-white: #ffffff;
  }
  * { margin: 0; padding: 0; box-sizing: border-box; }
  html, body {
    width: 1200px;
    height: 600px;
    overflow: hidden;
    background: var(--ink-black);
  }
  .cover-spread {
    display: flex;
    width: 1200px;
    height: 600px;
  }
  .cover {
    position: relative;
    width: 600px;
    height: 600px;
    overflow: hidden;
  }
  .smoke-art {
    position: absolute;
    inset: 0;
  }
  .cover--front .smoke-art {
    background:
      radial-gradient(ellipse 30% 35% at 50% 15%, rgba(255,255,255,0.95), rgba(255,255,255,0) 70%),
      radial-gradient(ellipse 70% 40% at 50% 88%, var(--ink-black) 0%, var(--smoke-dark) 60%, rgba(28,28,28,0) 100%),
      linear-gradient(180deg, var(--smoke-white) 0%, var(--smoke-light) 38%, var(--smoke-grey) 52%, var(--smoke-dark) 66%, var(--ink-black) 100%);
  }
  .cover--back .smoke-art {
    background:
      radial-gradient(ellipse 38% 60% at 50% 55%, var(--ink-black) 0%, var(--smoke-dark) 60%, rgba(28,28,28,0) 100%),
      linear-gradient(180deg, #222222 0%, #3a3a3a 30%, #8a8a8a 60%, #d8d8d8 100%);
  }
  .artist-mark {
    position: absolute;
    left: 0;
    right: 0;
    top: 222px;
    text-align: center;
    font-family: "Special Elite", "Courier New", monospace;
    font-size: 64px;
    line-height: 76px;
    letter-spacing: 6px;
    color: var(--mark-red);
  }
  .cover--back .artist-mark {
    color: var(--mark-red-back);
  }
  .title-rule {
    position: absolute;
    left: 174px;
    top: 478px;
    width: 252px;
    height: 1px;
    background: var(--type-white);
  }
  .artist-name {
    position: absolute;
    left: 0;
    right: 0;
    top: 490px;
    text-align: center;
    font-family: "Special Elite", "Courier New", monospace;
    font-size: 22px;
    line-height: 28px;
    font-weight: 400;
    letter-spacing: 3px;
    color: var(--type-white);
  }
</style>
</head>
<body>
  <main class="cover-spread">
    <section class="cover cover--front">
      <div class="smoke-art" role="img" aria-label="Mirrored abstract smoke and ink, bright white haze above fading into black"></div>
      <div class="artist-mark">DANE OLSK</div>
      <div class="title-rule"></div>
      <h1 class="artist-name">DANE OLSK</h1>
    </section>
    <section class="cover cover--back">
      <div class="smoke-art" role="img" aria-label="Mirrored abstract ink blot, dark centre spreading over pale grey corners"></div>
      <div class="artist-mark">DANE OLSK</div>
    </section>
  </main>
</body>
</html>
```